Stationary project for Velto Mobile Device training company
Stationary project for Velto Mobile Device training company - Electronics
Creative Brief
Use same font as used in my logo
Can use different fonts
Bright & Fun-filled
Dorian Welkett
PO Box 318 Medford, MA 02187
dorian@uPhaseMentor-example.com
www.uPhaseMentor-example.com

```html
<!DOCTYPE html>
<html lang="en">
<head>
<meta charset="utf-8">
<title>uPhase Mentor – Business Card</title>
<link rel="stylesheet" href="https://fonts.googleapis.com/css2?family=Open+Sans:wght@400;600;700&display=swap">
<style>
  :root {
    --stage: #9c9c9c;
    --card-dark: #1b1b1b;
    --card-light: #ffffff;
    --ink: #2a2a2a;
    --ink-soft: #666666;
    --brand-red: #c4161c;
    --brand-red-deep: #8e0e12;
    --band-dark: #151515;
  }
  * { box-sizing: border-box; margin: 0; padding: 0; }
  html, body { width: 1200px; height: 799px; overflow: hidden; }
  body {
    background: var(--stage);
    font-family: "Open Sans", Arial, sans-serif;
    display: flex;
    align-items: center;
    justify-content: center;
    gap: 60px;
  }
  .card {
    position: relative;
    width: 520px;
    height: 297px;
    border-radius: 18px;
    overflow: hidden;
  }
  .card--back {
    background: var(--card-dark);
    display: flex;
    align-items: center;
    justify-content: center;
    gap: 18px;
  }
  .brand-dot {
    width: 62px; height: 62px; border-radius: 50%;
    background: var(--brand-red);
    flex: none;
  }
  .brand-lockup { display: flex; flex-direction: column; }
  .brand-name {
    font-weight: 700;
    font-size: 30px;
    letter-spacing: 1px;
    text-transform: uppercase;
    line-height: 1.1;
  }
  .brand-tagline {
    font-size: 11px;
    letter-spacing: 2px;
    margin-top: 2px;
  }
  .card--back .brand-name { color: #ffffff; }
  .card--back .brand-tagline { color: #bdbdbd; }

  .card--front { background: var(--card-light); }
  .card--front .brand-lockup { position: absolute; left: 30px; top: 32px; }
  .card--front .brand-name { color: var(--ink); font-size: 26px; }
  .card--front .brand-tagline { color: var(--ink-soft); font-size: 10px; }
  .holder { position: absolute; left: 30px; top: 112px; }
  .holder__name { color: var(--brand-red); font-weight: 600; font-size: 20px; line-height: 1.1; }
  .holder__role { color: var(--ink-soft); font-size: 11px; margin-bottom: 12px; }
  .contact { list-style: none; font-size: 11px; color: var(--ink); }
  .contact li { display: flex; align-items: center; gap: 7px; margin-bottom: 4px; }
  .contact svg { width: 12px; height: 12px; fill: var(--brand-red); }
  .brand-circle {
    position: absolute; right: 48px; top: 48px;
    width: 150px; height: 150px; border-radius: 50%;
    background: var(--brand-red);
  }
  .footer-band { position: absolute; left: 0; bottom: 0; width: 520px; height: 60px; }
  .footer-band svg { position: absolute; inset: 0; }
  .footer-band__address, .footer-band__web {
    position: absolute; color: #ffffff; font-size: 10.5px; white-space: nowrap;
  }
  .footer-band__address { left: 30px; bottom: 9px; }
  .footer-band__web { right: 22px; bottom: 24px; }
</style>
</head>
<body>
  <section class="card card--back" aria-label="Card back">
    <span class="brand-dot"></span>
    <div class="brand-lockup">
      <span class="brand-name">uPhase Mentor</span>
      <span class="brand-tagline">Mobile Training Solutions</span>
    </div>
  </section>

  <section class="card card--front" aria-label="Card front">
    <div class="brand-lockup">
      <span class="brand-name">uPhase Mentor</span>
      <span class="brand-tagline">Mobile Training Solutions</span>
    </div>
    <div class="holder">
      <p class="holder__name">Dorian Welkett</p>
      <p class="holder__role">Vice President</p>
      <ul class="contact">
        <li>
          <svg viewBox="0 0 24 24"><path d="M6.6 10.8a15 15 0 0 0 6.6 6.6l2.2-2.2a1 1 0 0 1 1-.25 11.4 11.4 0 0 0 3.6.6 1 1 0 0 1 1 1V20a1 1 0 0 1-1 1A17 17 0 0 1 3 4a1 1 0 0 1 1-1h3.5a1 1 0 0 1 1 1c0 1.25.2 2.45.6 3.6a1 1 0 0 1-.25 1z"/></svg>
          555.014.2286
        </li>
        <li>
          <svg viewBox="0 0 24 24"><path d="M2 5h20v14H2zm2 2v.5l8 5 8-5V7l-8 5z"/></svg>
          dorian@uPhaseMentor-example.com
        </li>
      </ul>
    </div>
    <span class="brand-circle"></span>
    <div class="footer-band">
      <svg viewBox="0 0 520 60" preserveAspectRatio="none">
        <path d="M0 32 H250 C300 32 320 10 380 6 C430 2 480 4 520 0 V60 H0 Z" fill="var(--band-dark)"/>
        <path d="M250 32 C300 32 320 10 380 6 C430 2 480 4 520 0 V46 C470 46 430 44 380 44 C330 44 300 48 270 60 H250 Z" fill="var(--brand-red)"/>
        <path d="M330 46 C380 40 460 40 520 42 V46 C460 46 400 46 330 50 Z" fill="var(--brand-red-deep)"/>
      </svg>
      <span class="footer-band__address">PO Box 318 Tarnwick, NH 02187</span>
      <span class="footer-band__web">www.uPhaseMentor-example.com</span>
    </div>
  </section>
</body>
</html>
```